Fundraising Brochure Design for Environmental Organization

We need a fundraising brochure designed for the Ashby and Tillard Streamwarden. This is an environmental group that helps keep the Ashby and Tillard rivers open to the public and clean for swimming and fishing. The brochure will be used to help raise money for the organization. The brochure text, layout and image options, are given. Also included are two examples of brochures we like. The layout should be clean (not cluttered), easy to read, and attractive to look at. It should communicate the beauty of the rivers and encourage people to get involved.
Updates

Hello Everyone, Thank you for submitting so many wonderful designs!! We are working with our client to review each one. Next week we will contact you with feedback from the client, and let you know if they have any requests for changes to the designs before making the final decision. Have a great weekend!

Hello Designers, Thank you for submitting such wonderful designs. We will be meeting soon to discuss the designs with our client. Once we get feedback from them we will be in touch. Thank you for your patience.

Target Market(s)

The target audience for this brochure includes people who are rich homeowners, over 60 years old, who may have a vacation home, have a high-paying job, may own their own business, may be a doctor, lawyer, etc., dive a luxury car, and owns a boat or airplane.

The target audience also includes people who travel a lot, may be retired, even at a young age, and also younger people who are wealthy through inheritance.

Industry/Entity Type

Group

Requirements
Must have
• Must be a tri-fold brochure matching the dimensions provided in the Brochure Interior and Exterior Dimensions files.
Each page must include the text provided in the Fundraising Brochure Text file.
The logos listed in the Fundraising Brochure Text file are provided and must be included in the brochure where indicated.
Should not have
• There should be no pictures of pools.
Not all of the photos provided should be used in the brochure.
Do not edit the text.

```html
<!DOCTYPE html>
<html lang="en">
<head>
<meta charset="utf-8">
<title>Ashby and Tillard Streamwarden – Fundraising Brochure</title>
<link href="https://fonts.googleapis.com/css2?family=Oswald:wght@500;600&family=Patrick+Hand&family=Arimo:wght@400;700&display=swap" rel="stylesheet">
<style>
:root{
  --panel-blue:#5a92b6;
  --panel-blue-dark:#3f7ba2;
  --sky-top:#9cc6df;
  --sky-mid:#6fa3c4;
  --teal-dark:#1f5663;
  --teal-mid:#2f7484;
  --white:#ffffff;
  --cream:#f4e6c4;
  --orange:#f7941d;
  --yellow:#ffd81a;
  --lime:#f3e53a;
  --navy:#27408b;
  --map-land:#e2b7a6;
  --map-water:#8ea3dc;
}
*{box-sizing:border-box;margin:0;padding:0}
html,body{width:1200px;height:927px;overflow:hidden;background:#fff}
.brochure{position:relative;width:1200px;height:927px;overflow:hidden;font-family:"Arimo",Arial,sans-serif;color:var(--white)}
.panel{position:absolute;top:0;height:927px}
.panel-form{left:0;width:400px;background:linear-gradient(180deg,#6a9fc1 0%,var(--panel-blue) 45%,var(--panel-blue-dark) 100%)}
.panel-middle{left:400px;width:397px;background:linear-gradient(180deg,var(--sky-top) 0%,var(--sky-mid) 35%,var(--panel-blue-dark) 100%)}

/* form panel */
.form-title{position:absolute;left:70px;top:32px;font-size:19px;font-weight:700;line-height:25px}
.field{position:absolute;left:40px;font-size:16px;display:flex;align-items:flex-end;width:300px}
.field .rule{flex:1;border-bottom:1px solid var(--white);margin-left:8px;height:14px}
.field .rule.short{flex:0 0 auto}
.levels{position:absolute;left:38px;top:292px;list-style:none}
.levels li{display:flex;align-items:center;height:37.2px;font-size:18px;font-weight:700}
.box{width:18px;height:18px;border:1.5px solid var(--white);display:inline-block;margin-right:14px}
.levels .amt{width:67px}
.levels .top-tier{color:var(--cream)}
.pay-title{position:absolute;left:38px;top:575px;font-size:19px;font-weight:700}
.pay-options{position:absolute;left:40px;top:609px;display:flex;font-size:16px}
.pay-options span{display:flex;align-items:center;margin-right:12px}
.pay-options .box{margin-right:4px}
.nonprofit{position:absolute;left:36px;top:832px;width:340px;font-size:14.5px;line-height:20px}

/* middle panel */
.partner{position:absolute;display:flex;align-items:center;font-weight:700}
.partner-a{left:440px;top:55px;font-size:20px;color:#3a5a2c}
.partner-b{left:580px;top:103px;font-size:20px;color:#3f5f9e}
.partner-c{left:425px;top:150px;font-size:18px;color:var(--navy)}
.partner .dot{width:30px;height:30px;border-radius:50%;background:currentColor;margin-right:8px;opacity:.9}
.map{position:absolute;left:287px;top:210px;width:510px;height:547px;clip-path:polygon(60px 0,100% 0,100% 100%,0 100%,0 90px);filter:drop-shadow(0 6px 8px rgba(0,0,0,.4))}
.address{position:absolute;left:420px;top:778px;font-family:"Patrick Hand",cursive;font-style:normal;font-size:19px;line-height:20px;letter-spacing:.5px}
.address .web{font-family:"Arimo",Arial,sans-serif;font-weight:700;font-size:16px;letter-spacing:0}

/* help panel */
.help-photo{position:absolute;left:797px;top:0;width:403px;height:927px}
.headline-how{position:absolute;left:832px;top:22px;font-family:"Oswald",sans-serif;font-weight:600;font-size:100px;line-height:110px;color:var(--orange);transform:scaleX(.85) skewX(-8deg);transform-origin:left top}
.headline-canyou{position:absolute;left:987px;top:18px;font-family:"Oswald",sans-serif;font-weight:500;font-size:44px;line-height:56px;color:var(--orange);letter-spacing:3px}
.headline-help{position:absolute;left:960px;top:64px;font-family:"Oswald",sans-serif;font-weight:600;font-size:70px;line-height:70px;color:var(--yellow);letter-spacing:6px}
.intro{position:absolute;left:840px;top:141px;width:320px;font-family:"Patrick Hand",cursive;font-size:17px;line-height:19px;color:var(--lime);letter-spacing:1px;white-space:nowrap}
.body-copy{position:absolute;left:820px;width:370px;font-weight:700;font-size:13.4px;line-height:17px}
.body-copy.yellow{color:var(--lime)}
.lot{position:absolute;left:828px;top:412px;font-size:16px;font-weight:700;color:var(--lime);line-height:21px}
.without{position:absolute;left:865px;top:454px;font-size:26px;font-weight:700;color:var(--yellow)}
.join{position:absolute;left:860px;top:488px;width:330px;font-family:"Patrick Hand",cursive;font-size:20px;line-height:22px;color:var(--lime);font-style:italic;letter-spacing:.6px;white-space:nowrap}
.join span{display:block}
.join .love{padding-left:50px;font-size:27px;line-height:34px}
.headline-how2{position:absolute;left:848px;top:692px;font-family:"Oswald",sans-serif;font-weight:600;font-size:88px;line-height:96px;color:var(--orange);transform:scaleX(.85) skewX(-8deg);transform-origin:left top}
.how-steps{position:absolute;left:834px;top:795px;font-size:14.5px;font-weight:700;line-height:20px;color:var(--yellow)}
.how-steps .plain{color:var(--white)}
.how-steps .org{color:var(--orange);padding-left:4px}
</style>
</head>
<body>
<div class="brochure">

  <section class="panel panel-form">
    <h2 class="form-title">Please join or renew your<br>&nbsp;membership</h2>
    <div class="field" style="top:94px">Name:<span class="rule"></span></div>
    <div class="field" style="top:126px">Street:<span class="rule" style="margin-left:18px"></span></div>
    <div class="field" style="top:159px">City:<span class="rule short" style="width:70px;margin-left:2px"></span>&nbsp;State:<span class="rule short" style="width:34px;margin-left:2px"></span>Zip:<span class="rule" style="margin-left:2px"></span></div>
    <div class="field" style="top:191px">Phone:<span class="rule" style="margin-left:12px"></span></div>
    <div class="field" style="top:225px">email:<span class="rule" style="margin-left:10px"></span></div>

    <ul class="levels">
      <li><span class="box"></span><span class="amt">$35</span>Individual</li>
      <li><span class="box"></span><span class="amt">$50</span>Family</li>
      <li><span class="box"></span><span class="amt">$100</span>Supporter</li>
      <li><span class="box"></span><span class="amt">$250</span>Friend</li>
      <li><span class="box"></span><span class="amt">$500</span>Steward</li>
      <li class="top-tier"><span class="box"></span><span class="amt">$1000</span>Visionary</li>
      <li class="top-tier"><span class="box"></span><span class="amt">$5000</span>Legacy</li>
    </ul>

    <h3 class="pay-title">Payment Method:</h3>
    <div class="pay-options">
      <span><i class="box"></i>Check</span>
      <span><i class="box"></i>Nova</span>
      <span><i class="box"></i>QC</span>
    </div>

    <div class="field" style="top:675px;width:218px">Card #<span class="rule" style="margin-left:0"></span></div>
    <div class="field" style="top:711px;width:216px">Security Code<span class="rule" style="margin-left:0"></span></div>
    <div class="field" style="top:748px;width:212px">Exp. Date<span class="rule" style="margin-left:0"></span></div>
    <div class="field" style="top:784px;width:210px">Signature<span class="rule" style="margin-left:0"></span></div>

    <p class="nonprofit">Ashby/Tillard Streamwarden, Inc. is a 501 (c) 3<br>nonprofit organization, and all contributions<br>are tax deductible.</p>
  </section>

  <section class="panel panel-middle"></section>

  <div class="partner partner-a"><span class="dot"></span>Bay Stewards Coalition</div>
  <div class="partner partner-b"><span class="dot"></span>Stream Link</div>
  <div class="partner partner-c"><span class="dot"></span>Shoreline Guild Member</div>

  <svg class="map" role="img" aria-label="Map of the Ashby and Tillard rivers watershed with tributary streams and a mileage scale" viewBox="0 0 510 547">
    <defs>
      <linearGradient id="mapTone" x1="0" y1="0" x2="1" y2="1">
        <stop offset="0" stop-color="var(--map-land)"/>
        <stop offset=".55" stop-color="#d9b3b0"/>
        <stop offset="1" stop-color="var(--map-water)"/>
      </linearGradient>
    </defs>
    <rect width="510" height="547" fill="url(#mapTone)"/>
  </svg>

  <address class="address">
    Ashby/Tillard Streamwarden, Inc.<br>
    2150 Marsh Hollow Lane<br>
    Cove Point, MD 20699<br>
    410-555-0142<br>
    <span class="web">warden@ashbytillardstreams.org</span><br>
    <span class="web">www.ashbytillardstreams.org</span>
  </address>

  <svg class="help-photo" role="img" aria-label="Photo of young volunteers planting trees along a riverbank" viewBox="0 0 403 927">
    <defs>
      <linearGradient id="photoTone" x1="0" y1="0" x2=".4" y2="1">
        <stop offset="0" stop-color="#3e8a96"/>
        <stop offset=".45" stop-color="#2c6f7c"/>
        <stop offset=".75" stop-color="#24534a"/>
        <stop offset="1" stop-color="#1a3a33"/>
      </linearGradient>
    </defs>
    <rect width="403" height="927" fill="url(#photoTone)"/>
  </svg>

  <div class="headline-how">How</div>
  <div class="headline-canyou">can you</div>
  <div class="headline-help">HELP</div>

  <p class="intro">Just as the rivers need the<br>Streamwarden's help, the Streamwarden<br>needs your help. Your financial gift<br>is vital to the success of our efforts.</p>

  <p class="body-copy yellow" style="top:238px">We will leverage your tax-deductible contribution<br>&nbsp;up to four times its value in grants</p>
  <p class="body-copy" style="top:278px">from corporations, private foundations, as well<br>as county, state and federal resources.</p>
  <p class="body-copy yellow" style="top:321px">Every dollar you give means we can do $5 worth<br>&nbsp;of work planting trees, growing oysters, restoring<br>&nbsp;marshes and streambeds, creating wetlands and<br>&nbsp;living shorelines that protect the Ashby and Tillard<br>&nbsp;Rivers for generations to come.</p>

  <p class="lot">There's a lot to do,<br>&nbsp;&nbsp;&nbsp;&nbsp;&nbsp;&nbsp;&nbsp;and we couldn't do all we do</p>
  <p class="without">without you.</p>
  <p class="join">
    <span style="padding-left:13px">Join us as a volunteer, become</span>
    <span style="padding-left:5px">a member, or consider making a</span>
    <span style="padding-left:18px">meaningful financial contribution</span>
    <span style="padding-left:24px">to help us protect these rivers that</span>
    <span class="love">we all love.</span>
  </p>

  <div class="headline-how2">How?</div>
  <p class="how-steps">Log on to <span class="plain">www.ashbytillardstreams.org</span><br>or call <span class="plain">410-555-0142.</span><br>Or fill out the attached form and send it in<br>&nbsp;with a check made out to:<br><span class="org">Ashby/Tillard Streamwarden, Inc.</span></p>

</div>
</body>
</html>
```